Truck Driver Pay - Small Infographic

I need a very small, compact infographic to illustrate the differences in pay for a solo truck driver vs. team truck drivers. This illustration will be viewed on the web exclusively. I have sketched out an idea with all of the content that must be included. I just need a designer's touch.

The attached 'mock up' contains the information to be illustrated/communicated by this infographic.

Target Market(s)

Blue collar employee males ages 18-49 with high school education

Requirements
Must have
• I need 2 versions of the graphic:
• 1) 600 pixels wide for desktop presentation
• 2) 300 pixels wide with vertical scroll for mobile.
• I also require the native .psd or .ai files used to create this infographic.

```html
<!DOCTYPE html>
<html lang="en">
<head>
<meta charset="utf-8">
<title>Understanding Driver Pay</title>
<link rel="stylesheet" href="https://fonts.googleapis.com/css2?family=Open+Sans:wght@300;400;600;700;800&display=swap">
<style>
  :root{
    --teal:#22b7b4;
    --blue:#1b6da8;
    --dark:#3f3f3f;
    --ink:#3a3a3a;
    --light:#dcdcdc;
    --page:#f4f4f4;
    --white:#ffffff;
    --mid:#8a8a8a;
  }
  *{box-sizing:border-box;margin:0;padding:0}
  html,body{width:686px;height:1200px;overflow:hidden;background:var(--page)}
  body{font-family:"Open Sans",Arial,sans-serif;color:var(--ink)}
  .canvas{position:relative;width:686px;height:1200px;background:var(--page)}
  .abs{position:absolute}

  .header{left:13px;top:13px;width:660px;height:167px;background:var(--light);text-align:center}
  .title-top{position:absolute;left:0;right:0;top:50px;font-weight:300;font-size:42px;line-height:1;color:var(--teal);letter-spacing:.5px}
  .title-main{position:absolute;left:0;right:0;top:96px;font-weight:700;font-size:40px;line-height:1;color:var(--ink)}

  .band{left:13px;top:180px;width:660px;height:21px;background:linear-gradient(90deg,var(--teal),var(--blue))}
  .col-solo{left:13px;top:201px;width:330px;height:892px;background:var(--light)}
  .col-team{left:343px;top:201px;width:330px;height:892px;background:var(--dark)}

  .col-title{font-weight:700;font-size:17px;line-height:1}
  .col-sub{font-weight:400;font-size:13px;line-height:1}
  .on-dark{color:var(--light)}

  .art{border-radius:4px}
  .art-truck-solo{left:64px;top:313px;width:116px;height:146px;background:var(--dark)}
  .art-truck-team{left:373px;top:313px;width:124px;height:146px;background:var(--light)}
  .art-person{left:244px;top:350px;width:52px;height:112px;background:var(--dark);border-radius:26px 26px 6px 6px}
  .art-pair{left:545px;top:350px;width:103px;height:112px;background:var(--light);border-radius:30px 30px 6px 6px}

  .plus{width:30px;height:30px}
  .plus::before,.plus::after{content:"";position:absolute;background:currentColor}
  .plus::before{left:11px;top:0;width:8px;height:30px}
  .plus::after{left:0;top:11px;width:30px;height:8px}

  .tag{width:110px;height:52px;text-align:center;font-weight:600;font-size:14px;line-height:17px;padding-top:9px}
  .tag::after{content:"";position:absolute;left:46px;bottom:-10px;border-left:9px solid transparent;border-right:9px solid transparent;border-top:10px solid currentColor}
  .tag-solo{left:127px;top:504px;background:var(--dark);color:var(--white)}
  .tag-solo::after{border-top-color:var(--dark)}
  .tag-team{left:454px;top:504px;background:var(--light);color:var(--ink)}
  .tag-team::after{border-top-color:var(--light)}

  .miles{font-weight:700;font-size:35px;line-height:1}
  .label{font-weight:700;font-size:15px;line-height:1}
  .mini-truck{width:52px;height:17px;border-radius:2px}
  .times{font-weight:600;font-size:22px;line-height:1}
  .rate{width:66px;height:66px;border-radius:50%;border:4px solid currentColor;display:flex;align-items:center;justify-content:center;font-weight:700;font-size:27px}
  .peaks{width:134px;height:56px;background:linear-gradient(135deg,var(--blue),var(--teal) 55%,var(--dark))}
  .rule{height:5px}
  .pay{font-weight:700;font-size:38px;line-height:1}
  .pay-label{font-weight:700;font-size:15px;line-height:1}
  .bag{width:36px;height:48px;border-radius:10px 10px 14px 14px}
  .each{left:405px;top:738px;width:42px;height:42px;border-radius:50%;background:var(--light);color:var(--ink);font-weight:700;font-size:10px;line-height:11px;text-align:center;padding-top:10px}

  .road{left:13px;top:820px;width:660px;height:273px}

  .bubble{border:2px solid var(--light);border-radius:8px;font-weight:700;font-size:11.5px;line-height:15px;padding:9px 12px}
  .bubble-solo{left:165px;top:825px;width:164px;height:92px;background:var(--dark);color:var(--white)}
  .bubble-team{left:416px;top:823px;width:245px;height:96px;background:var(--light);color:var(--ink);border-color:var(--white);font-size:11px;line-height:14px}
  .note{font-weight:700;font-size:11px;line-height:14.5px;padding:10px 16px}
  .note-solo{left:41px;top:948px;width:216px;height:71px;background:var(--dark);color:var(--white)}
  .note-team{left:373px;top:948px;width:217px;height:71px;background:var(--light);color:var(--ink)}
  .stop{left:80px;top:848px;width:70px;height:66px}
  .art-walker{left:43px;top:896px;width:22px;height:48px;background:var(--dark);border-radius:11px 11px 3px 3px}
  .art-swap{left:358px;top:870px;width:46px;height:74px;background:var(--light);border-radius:6px}

  .footnote{left:200px;top:1055px;width:286px;height:23px;background:var(--dark);color:var(--white);font-size:10.5px;line-height:23px;padding-left:12px}
  .footnote b{margin-right:10px}

  .bottom{left:13px;top:1093px;width:660px;height:95px;background:linear-gradient(90deg,var(--teal),var(--blue));text-align:center;color:var(--white)}
  .bottom h2{position:absolute;left:0;right:0;top:17px;font-weight:700;font-size:28px;line-height:1}
  .bottom p{position:absolute;left:0;right:0;top:49px;font-weight:700;font-size:13px;line-height:1}
</style>
</head>
<body>
<div class="canvas">
  <div class="abs header">
    <div class="title-top">UNDERSTANDING</div>
    <div class="title-main">DRIVER PAY</div>
  </div>
  <div class="abs band"></div>
  <div class="abs col-solo"></div>
  <div class="abs col-team"></div>

  <svg class="abs" style="left:13px;top:180px" width="660" height="95" viewBox="0 0 660 95" aria-hidden="true">
    <path d="M0 0 H40 V52 H95 V36 L122 64 L95 92 V76 H18 V21 H0 Z" fill="var(--teal)"/>
    <path d="M660 0 H620 V52 H565 V36 L538 64 L565 92 V76 H642 V21 H660 Z" fill="var(--blue)"/>
  </svg>

  <div class="abs col-title" style="left:147px;top:225px">SOLO DRIVER PAY</div>
  <div class="abs col-sub" style="left:147px;top:246px">1 TRUCK 1 DRIVER</div>
  <div class="abs col-title on-dark" style="left:369px;top:225px">TEAM DRIVER PAY</div>
  <div class="abs col-sub on-dark" style="left:369px;top:246px">1 TRUCK 2 DRIVERS</div>

  <div class="abs art art-truck-solo" role="img" aria-label="Front view of a truck"></div>
  <div class="abs plus" style="left:192px;top:378px;color:var(--dark)"></div>
  <div class="abs art-person" role="img" aria-label="One driver figure"></div>
  <div class="abs art art-truck-team" role="img" aria-label="Front view of a truck"></div>
  <div class="abs plus" style="left:503px;top:378px;color:var(--light)"></div>
  <div class="abs art-pair" role="img" aria-label="Two driver figures"></div>

  <div class="abs tag tag-solo">Example<br>pay check</div>
  <div class="abs tag tag-team">Example<br>pay check</div>

  <!-- solo paycheck -->
  <div class="abs miles" style="left:55px;top:586px">2500</div>
  <div class="abs label" style="left:153px;top:602px">weekly miles driven</div>
  <div class="abs mini-truck" style="left:261px;top:576px;background:var(--dark)" role="img" aria-label="Small truck icon"></div>
  <div class="abs times" style="left:41px;top:650px">x</div>
  <div class="abs rate" style="left:70px;top:629px;color:var(--dark)">.26</div>
  <div class="abs peaks" style="left:154px;top:622px" role="img" aria-label="Mountain range graphic"></div>
  <div class="abs label" style="left:167px;top:688px">mileage rate *</div>
  <div class="abs rule" style="left:43px;top:713px;width:270px;background:var(--dark)"></div>
  <div class="abs pay" style="left:106px;top:738px">$650</div>
  <div class="abs pay-label" style="left:108px;top:777px">weekly pay</div>
  <div class="abs bag" style="left:214px;top:742px;background:var(--dark)" role="img" aria-label="Money bag icon"></div>

  <!-- team paycheck -->
  <div class="abs miles on-dark" style="left:384px;top:586px">4300</div>
  <div class="abs label on-dark" style="left:484px;top:602px">weekly miles driven</div>
  <div class="abs mini-truck" style="left:588px;top:576px;background:var(--light)" role="img" aria-label="Small truck icon"></div>
  <div class="abs times on-dark" style="left:372px;top:650px">x</div>
  <div class="abs rate on-dark" style="left:400px;top:629px;font-size:24px;border-color:var(--light)">.175</div>
  <div class="abs peaks" style="left:484px;top:622px" role="img" aria-label="Mountain range graphic"></div>
  <div class="abs label on-dark" style="left:497px;top:688px">mileage rate *</div>
  <div class="abs rule" style="left:373px;top:713px;width:270px;background:var(--light)"></div>
  <div class="abs each">each<br>driver</div>
  <div class="abs pay on-dark" style="left:466px;top:738px">$752</div>
  <div class="abs pay-label on-dark" style="left:468px;top:777px">weekly pay</div>
  <div class="abs bag" style="left:570px;top:742px;background:var(--light)" role="img" aria-label="Money bag icon"></div>

  <!-- road -->
  <svg class="abs road" viewBox="0 0 660 273" aria-hidden="true">
    <polygon points="0,28 330,98 330,120 0,50" fill="var(--teal)"/>
    <polygon points="0,50 330,120 330,142 0,72" fill="var(--blue)"/>
    <line x1="0" y1="50" x2="330" y2="120" stroke="var(--white)" stroke-width="2" stroke-dasharray="14 10"/>
    <polygon points="330,70 660,130 660,152 330,92" fill="var(--teal)"/>
    <polygon points="330,92 660,152 660,174 330,114" fill="var(--blue)"/>
    <line x1="330" y1="92" x2="660" y2="152" stroke="var(--white)" stroke-width="2" stroke-dasharray="14 10"/>
  </svg>

  <svg class="abs stop" viewBox="0 0 70 66" aria-hidden="true">
    <polygon points="18,2 52,2 68,33 52,64 18,64 2,33" fill="var(--dark)"/>
    <rect x="27" y="18" width="16" height="28" rx="6" fill="var(--light)"/>
  </svg>
  <div class="abs bubble bubble-solo">When a solo driver needs to take his required break, the truck has to stop rolling.</div>
  <div class="abs art-walker" role="img" aria-label="Single driver figure"></div>
  <div class="abs note note-solo">A solo driver can drive a limited amount of miles due to mandated breaks and safety regulations.</div>
  <svg class="abs" style="left:270px;top:995px" width="44" height="48" viewBox="0 0 44 48" aria-hidden="true">
    <path d="M22 2 L40 8 V22 C40 34 32 42 22 46 C12 42 4 34 4 22 V8 Z" fill="var(--dark)"/>
    <path d="M13 24 L20 31 L32 17" fill="none" stroke="var(--light)" stroke-width="4" stroke-linecap="round" stroke-linejoin="round"/>
  </svg>

  <div class="abs bubble bubble-team">Team drivers alternate driving duties so the truck covers more miles. When Driver 1 needs to take his required break, Driver 2 takes over the driving duties until his required break and they switch places agian.</div>
  <div class="abs art-swap" role="img" aria-label="Two drivers switching places with a clock"></div>
  <div class="abs note note-team">The truck keeps rolling and both drivers are paid for all of the combined miles the truck has been driven.</div>
  <svg class="abs" style="left:599px;top:995px" width="46" height="46" viewBox="0 0 46 46" aria-hidden="true">
    <circle cx="23" cy="23" r="20" fill="var(--light)" stroke="var(--white)" stroke-width="3"/>
    <circle cx="23" cy="23" r="14" fill="none" stroke="var(--mid)" stroke-width="2" stroke-dasharray="2 3"/>
    <line x1="23" y1="23" x2="32" y2="14" stroke="var(--dark)" stroke-width="3" stroke-linecap="round"/>
  </svg>

  <div class="abs footnote"><b>*</b>Weekly mileage will vary. For illustration only</div>

  <div class="abs bottom">
    <h2>Bottom Line:</h2>
    <p>The More Miles Your Truck Goes, The More Money You Make.</p>
  </div>
</div>
</body>
</html>
```